Corvane Supplies Business Card

Professional business card that stand out to our potential customers. Front and back with clean modern design

Industry/Entity Type

Oil and gas

Contact Information for Business Card

Name, address, website , office phone and cell number

Requirements
Must have
• Editable files for each employee

```html
<!DOCTYPE html>
<html lang="en">
<head>
<meta charset="utf-8">
<title>Corvane Supplies Business Card</title>
<link href="https://fonts.googleapis.com/css2?family=Poppins:wght@400;500;700&display=swap" rel="stylesheet">
<style>
  :root {
    --bg: #c6c6c6;
    --card: #f6f6f6;
    --card-edge: #ffffff;
    --red: #e31b23;
    --blue: #12a5c9;
    --ink: #2a2a2a;
  }
  * { margin: 0; padding: 0; box-sizing: border-box; }
  html, body {
    width: 1200px; height: 864px; overflow: hidden;
    background: var(--bg);
    font-family: "Poppins", sans-serif;
  }
  .stage {
    position: relative; width: 1200px; height: 864px;
    display: flex; align-items: center; justify-content: center; gap: 40px;
  }
  .card {
    position: relative;
    width: 540px; height: 309px;
    border-radius: 40px;
    background: linear-gradient(135deg, var(--card-edge), var(--card));
    box-shadow: 0 6px 18px rgba(0,0,0,0.12);
    overflow: hidden;
  }
  /* back side */
  .card--back {
    display: flex; align-items: center; justify-content: center;
  }
  .brand {
    display: flex; align-items: center; gap: 12px;
  }
  .brand__mark {
    width: 22px; height: 22px; background: var(--red);
  }
  .brand__name {
    color: var(--red); font-weight: 700; letter-spacing: 0.04em;
    text-transform: uppercase;
  }
  .card--back .brand__name { font-size: 30px; }
  /* front side */
  .card--front .brand {
    position: absolute; left: 56px; top: 62px;
  }
  .card--front .brand__mark { width: 16px; height: 16px; }
  .card--front .brand__name { font-size: 22px; }
  .person {
    position: absolute; right: 290px; top: 150px; text-align: right;
  }
  .person__role {
    font-size: 13px; font-weight: 500; color: var(--ink); letter-spacing: 0.06em;
  }
  .person__name {
    font-size: 22px; font-weight: 700; color: var(--red);
    letter-spacing: 0.03em; white-space: nowrap; line-height: 1.1;
  }
  .divider {
    position: absolute; left: 268px; top: 148px;
    width: 1.5px; height: 84px; background: var(--ink);
  }
  .contacts {
    position: absolute; left: 284px; top: 150px; list-style: none;
  }
  .contacts li {
    display: flex; align-items: center; gap: 8px;
    font-size: 13px; color: var(--ink); height: 20px; letter-spacing: 0.02em;
  }
  .contacts svg { width: 12px; height: 12px; flex: none; }
</style>
</head>
<body>
<main class="stage">
  <section class="card card--back" aria-label="Card back">
    <div class="brand">
      <span class="brand__mark"></span>
      <span class="brand__name">Corvane Supplies</span>
    </div>
  </section>

  <section class="card card--front" aria-label="Card front">
    <div class="brand">
      <span class="brand__mark"></span>
      <span class="brand__name">Corvane Supplies</span>
    </div>

    <div class="person">
      <p class="person__role">CEO</p>
      <p class="person__name">MARISOL QUENTRY</p>
    </div>

    <span class="divider"></span>

    <ul class="contacts">
      <li>
        <svg viewBox="0 0 12 12"><circle cx="6" cy="6" r="6" fill="#e31b23"/><path d="M6 2.6a2 2 0 0 0-2 2c0 1.5 2 4 2 4s2-2.5 2-4a2 2 0 0 0-2-2z" fill="#fff"/><circle cx="6" cy="4.6" r="0.7" fill="#e31b23"/></svg>
        4120 Harbor Ln
      </li>
      <li>
        <svg viewBox="0 0 12 12"><circle cx="6" cy="6" r="6" fill="#e31b23"/><path d="M4 3.2l1 1.1-.6.8c.4.9 1.1 1.6 2 2l.8-.6 1.1 1-.6 1c-2.2-.2-4.1-2.1-4.3-4.3z" fill="#fff"/></svg>
        555 0142 7788
      </li>
      <li>
        <svg viewBox="0 0 12 12"><circle cx="6" cy="6" r="6" fill="#e31b23"/><rect x="3" y="4" width="6" height="4.2" fill="none" stroke="#fff" stroke-width="0.9"/><path d="M3 4l3 2.3L9 4" fill="none" stroke="#fff" stroke-width="0.9"/></svg>
        marisol@corvane.com
      </li>
      <li>
        <svg viewBox="0 0 12 12"><circle cx="6" cy="6" r="6" fill="#e31b23"/><circle cx="6" cy="6" r="3" fill="none" stroke="#fff" stroke-width="0.8"/><path d="M3 6h6M6 3c-1.3 1.6-1.3 4.4 0 6M6 3c1.3 1.6 1.3 4.4 0 6" fill="none" stroke="#fff" stroke-width="0.7"/></svg>
        www.corvane.com
      </li>
    </ul>
  </section>
</main>
</body>
</html>
```